MarnoT Designs

To have a blog that is interactive and shows products that I produce, with the ability to direct people to ViewLoop and Crafto
Updates

I not only do papercrafting but also do sublimition on T-shirts, and other items. I do the designs for all of them. So I need to have pages to decifer these.

I have logo's done. and can provide them.

Target Market(s)

Handmade cards, home projects, sublimiated items (shirts, cups, dog items)

Industry/Entity Type

Gift Shop

Number of Pages Required

4 page

Font styles to use
Serif

Requirements
Must have
• easy to operate for everyone, with good directions, connections to Crafto shop and ViewLoop, along with shopping from suppliers
Nice to have
• I would like the site to be one that clean but happy feeling, one that people will remember and return to. If someone is looking at something specific, maybe a new page to open
Should not have
• a confusing site.

```html
<!DOCTYPE html>
<html lang="en">
<head>
<meta charset="utf-8">
<title>MarnoT Designs</title>
<link rel="stylesheet" href="https://fonts.googleapis.com/css2?family=Lobster&family=Roboto:wght@400;500;700&family=Roboto+Slab:wght@400;500&family=Noto+Serif&display=swap">
<style>
:root{
  --pink:#f7708d;
  --pink-footer:#fb7b93;
  --purple:#8a5cd8;
  --lilac:#dccbf5;
  --ink:#2a2a2a;
  --text:#444;
  --muted:#9a9a9a;
  --band:#f7f6f3;
  --white:#fff;
}
*{margin:0;padding:0;box-sizing:border-box}
html,body{width:1200px;height:2531px;overflow:hidden;background:var(--white)}
body{position:relative;font-family:'Roboto',sans-serif;color:var(--text)}
.abs{position:absolute}

/* nav */
.nav{left:0;top:0;width:1200px;height:75px;background:var(--white)}
.nav a{position:absolute;top:33px;font-family:'Noto Serif',serif;font-size:13px;color:#444;text-decoration:none}
.brand{position:absolute;left:548px;top:24px;font-family:'Noto Serif',serif;font-size:20px;color:var(--purple);white-space:nowrap}

/* hero */
.hero{left:0;top:75px;width:1200px;height:525px;background:linear-gradient(90deg,#ee7798 0%,#eda2a2 50%,#ecd0a9 100%);overflow:hidden}
.hero h1{position:absolute;left:150px;top:118px;font-family:'Lobster',cursive;font-weight:400;font-size:68px;line-height:80px;color:var(--white)}
.hero p{position:absolute;left:150px;top:290px;width:380px;font-size:15px;line-height:25px;color:var(--white)}
.hero .btn{position:absolute;left:149px;top:366px;width:174px;height:38px;background:var(--white);color:var(--pink);font-size:15px;line-height:38px;text-align:center;border-radius:2px}
.hero-art{position:absolute;left:545px;top:50px;width:640px;height:520px;background:linear-gradient(135deg,#f6f1ec 0%,#f3d6d6 55%,#f7e48a 100%);transform:rotate(-10deg);transform-origin:left top;border-radius:6px;opacity:.9}

/* services */
.service{top:672px;width:240px;text-align:center}
.service .icon{width:54px;height:54px;margin:0 auto;border-radius:50%;background:var(--lilac);display:flex;align-items:center;justify-content:center;color:var(--purple);font-family:'Noto Serif',serif;font-size:20px}
.service h3{margin-top:14px;font-family:'Noto Serif',serif;font-weight:400;font-size:17px;color:var(--ink)}
.service p{margin-top:8px;font-size:12px;line-height:19px;color:#444}
.service .outline{display:inline-block;margin-top:17px;width:118px;height:31px;border:2px solid var(--purple);border-radius:16px;color:var(--purple);font-size:14px;line-height:27px}

/* section heads */
.sec-head{left:0;width:1200px;text-align:center}
.sec-head h2{font-family:'Lobster',cursive;font-weight:400;font-size:31px;color:var(--ink)}
.sec-head p{margin-top:8px;font-family:'Noto Serif',serif;font-size:15.5px;color:#333}

/* tiles */
.tile{top:1040px;width:301px;height:205px;border-radius:3px;display:flex;align-items:center;justify-content:center;font-family:'Roboto Slab',serif;font-size:22px;color:var(--white)}
.tile.yellow{left:117px;background:linear-gradient(135deg,#f8e28e,#f5d77a)}
.tile.lilac{left:448px;background:linear-gradient(135deg,#dccdf7,#cdb9f2)}
.tile.rose{left:780px;background:linear-gradient(135deg,#f19aae,#eb8199)}

/* about */
.about{left:0;top:1295px;width:1200px;height:527px;background:var(--band)}
.about-photo{position:absolute;left:117px;top:50px;width:300px;height:425px;background:linear-gradient(180deg,#5d7a4c 0%,#c99a78 45%,#e9d4cc 100%);border-radius:2px}
.about h2{position:absolute;left:509px;top:53px;font-family:'Lobster',cursive;font-weight:400;font-size:30px;color:var(--ink)}
.about .copy{position:absolute;left:510px;top:117px;width:565px;font-size:12.3px;line-height:20.3px;color:#444}
.about .copy p+p{margin-top:24px}
.about .btn{position:absolute;left:509px;top:409px;width:167px;height:46px;border-radius:23px;background:var(--pink);color:var(--white);font-weight:500;font-size:15px;line-height:46px;text-align:center}

/* blog cards */
.card{top:1975px;width:245px;height:280px;background:var(--white);box-shadow:0 2px 10px rgba(0,0,0,.07);border-radius:3px;overflow:hidden}
.card .thumb{height:152px}
.card h4{margin:16px 17px 0;font-family:'Noto Serif',serif;font-weight:400;font-size:15px;color:var(--ink)}
.card p{margin:9px 17px 0;font-size:11.5px;line-height:17px;color:#444}
.card .date{margin-top:17px;font-size:11px;color:var(--muted)}

/* footer */
.footer{left:0;top:2305px;width:1200px;height:226px;background:var(--pink-footer);color:var(--white)}
.footer h5{position:absolute;top:48px;font-weight:500;font-size:17px}
.footer .col{position:absolute;top:86px;font-size:12px;line-height:22px}
.footer .col span{display:block}
.footer .social span{display:flex;align-items:center;gap:7px}
.footer .social i{width:7px;height:7px;border-radius:50%;background:var(--white);display:inline-block}
.news-input{position:absolute;left:807px;top:140px;width:168px;height:24px;background:var(--white);color:#b5b5b5;font-size:10px;line-height:24px;padding-left:8px}
.news-btn{position:absolute;left:975px;top:140px;width:75px;height:24px;background:#f25a7a;color:var(--white);font-size:10.5px;font-weight:500;line-height:24px;text-align:center}
.footer .rule{position:absolute;left:0;top:193px;width:1200px;height:1px;background:rgba(255,255,255,.35)}
.footer .copyright{position:absolute;left:0;top:206px;width:1200px;text-align:center;font-size:12px}
</style>
</head>
<body>

<header class="abs nav">
  <a style="left:192px">Home</a>
  <a style="left:258px">Papercraft</a>
  <a style="left:348px">Sublimation</a>
  <a style="left:449px">About Me</a>
  <div class="brand">MarnoT Designs</div>
  <a style="left:724px">Products I Use</a>
  <a style="left:837px">Blog</a>
  <a style="left:893px">Videos</a>
  <a style="left:964px">Contact</a>
</header>

<section class="abs hero">
  <h1>Papercraft &amp;<br>Sublimation</h1>
  <p>Lorem ipsum dolor sit amet, consectetur adipisicing elit, sed do eiusmod tempor incididunt</p>
  <div class="btn">Read Latest Posts</div>
  <div class="hero-art" role="img" aria-label="Photo of two handmade floral greeting cards"></div>
</section>

<div class="abs service" style="left:92px">
  <div class="icon"><svg width="22" height="22" viewBox="0 0 22 22" fill="none" stroke="currentColor" stroke-width="1.6"><rect x="5" y="3" width="12" height="16" rx="1"/><path d="M8 8h6M8 11h6M8 14h4"/></svg></div>
  <h3>Paper Craft</h3>
  <p>Lorem ipsum dolor avdipiscing elit,<br>ssmod tempor incididunt ut labore</p>
  <span class="outline">Visit Now</span>
</div>
<div class="abs service" style="left:355px">
  <div class="icon"><svg width="24" height="22" viewBox="0 0 24 22" fill="none" stroke="currentColor" stroke-width="1.6" stroke-linejoin="round"><path d="M8 3 3 6l2 4 2-1v10h10V9l2 1 2-4-5-3c-1 2-2 3-4 3S9 5 8 3z"/></svg></div>
  <h3>Sublimation</h3>
  <p>Lorem ipsum dolor avdipiscing elit,<br>ssmod tempor incididunt ut labore</p>
  <span class="outline">Visit Now</span>
</div>
<div class="abs service" style="left:612px">
  <div class="icon"><svg width="24" height="20" viewBox="0 0 24 20" fill="none" stroke="currentColor" stroke-width="1.6"><rect x="2" y="3" width="20" height="14" rx="3"/><path d="M10 7v6l5-3z" fill="currentColor"/></svg></div>
  <h3>ViewLoop</h3>
  <p>Lorem ipsum dolor avdipiscing elit,<br>ssmod tempor incididunt ut labore</p>
  <span class="outline">Visit Now</span>
</div>
<div class="abs service" style="left:863px">
  <div class="icon">C</div>
  <h3>Crafto</h3>
  <p>Lorem ipsum dolor avdipiscing elit,<br>ssmod tempor incididunt ut labore</p>
  <span class="outline">Visit Now</span>
</div>

<div class="abs sec-head" style="top:925px">
  <h2>Lorem Ipsum</h2>
  <p>Lorem ipsum dolor sit amet, consectetur adipiscing</p>
</div>

<div class="abs tile yellow" role="img" aria-label="Craft desk photo with tools and paper">Videos</div>
<div class="abs tile lilac" role="img" aria-label="Photo of handmade greeting cards">Blogs</div>
<div class="abs tile rose" role="img" aria-label="Photo of a classroom craft session">Online Classes</div>

<section class="abs about">
  <div class="about-photo" role="img" aria-label="Portrait photo of the designer in front of green leaves"></div>
  <h2>About Me</h2>
  <div class="copy">
    <p>Well, MarnoT is a mother of three grown children, a daughter and two sons a daughter-in-law, and a grandmother of two gorgeous little ones, both are very special to me. Plus, one more on it way! I am currently on sick leave from work, due to an automobile accident last year. One being a concussion, and mobility of my neck.&nbsp; I also live with several disorders, Crohn's, Gastroparesis, Arterial Septal Defect, just to name a few. But, these don't get me down, unless you put me in the hospital and disrupt my days. That is right, I hate to be disrupted.</p>
    <p>The cards that I make are donated. I donate or give them to people all the time. I carry them with me most times, and share them with those willing to share. So making cards, and donating them has been very good for me.I would love to see some type of program in Canada where cards are donated to teachers and school councillors so that they can share these cards with students no matter what their reason. You see, I do believe that cards brighten the world and no matter what type of card they all will bring people together. Even when they are miles apart.</p>
  </div>
  <div class="btn">Read More</div>
</section>

<div class="abs sec-head" style="top:1860px">
  <h2>Latest Blogs</h2>
  <p>Lorem ipsum dolor sit amet, consectetur adipiscing</p>
</div>

<article class="abs card" style="left:76px">
  <div class="thumb" role="img" aria-label="Photo of a colourful birthday card" style="background:linear-gradient(135deg,#f7f3ef,#f3c6d4)"></div>
  <h4>Birthday Card</h4>
  <p>Lorem ipsum dolor sit&nbsp; consectetur<br>adipiscing elit, sed do mod tempor</p>
  <p class="date">Posted on 17th Feburary 2021</p>
</article>
<article class="abs card" style="left:343px">
  <div class="thumb" role="img" aria-label="Photo of a hand holding a printed coffee mug" style="background:linear-gradient(135deg,#e9e6e3,#f7f5f3)"></div>
  <h4>Coffee Mug Sublimation</h4>
  <p>Lorem ipsum dolor sit&nbsp; consectetur<br>adipiscing elit, sed do mod tempor</p>
  <p class="date">Posted on 17th Feburary 2021</p>
</article>
<article class="abs card" style="left:611px">
  <div class="thumb" role="img" aria-label="Photo of a yellow printed T-shirt" style="background:linear-gradient(135deg,#e7b23c,#d79a2a)"></div>
  <h4>Humble and Kind</h4>
  <p>Lorem ipsum dolor sit&nbsp; consectetur<br>adipiscing elit, sed do mod tempor</p>
  <p class="date">Posted on 17th Feburary 2021</p>
</article>
<article class="abs card" style="left:878px">
  <div class="thumb" role="img" aria-label="Photo of a botanical thank you card" style="background:linear-gradient(135deg,#eef0ee,#dfe7e3)"></div>
  <h4>Thank You Card</h4>
  <p>Lorem ipsum dolor sit&nbsp; consectetur<br>adipiscing elit, sed do mod tempor</p>
  <p class="date">Posted on 17th Feburary 2021</p>
</article>

<footer class="abs footer">
  <h5 style="left:151px">MarnoT Designs</h5>
  <div class="col" style="left:150px;top:90px;width:190px;line-height:19px">Lorem ipsum dolor sit amet, consectetur adipiscing elit, sed do eiusmod tempor incididunt ut labore et dolore magna aliqua.</div>

  <h5 style="left:387px">Quick Links</h5>
  <div class="col" style="left:388px"><span>Lorem Ipsum</span><span>Lorem Ipsum</span><span>Lorem Ipsum</span><span>Lorem Ipsum</span></div>

  <h5 style="left:529px">Quick Links</h5>
  <div class="col" style="left:529px"><span>Lorem Ipsum</span><span>Lorem Ipsum</span><span>Lorem Ipsum</span><span>Lorem Ipsum</span></div>

  <h5 style="left:671px">Follow Me</h5>
  <div class="col social" style="left:672px"><span><i></i>Friendwall</span><span><i></i>Chirpline</span><span><i></i>Snapgrid</span><span><i></i>ViewLoop</span></div>

  <h5 style="left:808px">Subscribe to Newsletter</h5>
  <div class="col" style="left:805px;width:250px;line-height:19px">Lorem ipsum dolor sit amet, consectetur adipiscing elit, sed do eiusmod tempor</div>
  <div class="news-input">Enter your Email</div>
  <div class="news-btn">Subscribe</div>

  <div class="rule"></div>
  <div class="copyright">Copyright © MarnoT Designs 2021</div>
</footer>

</body>
</html>
```